TORVALE: Social Media Post COVID-19 & Flu #2

- Please use or create a similar design as before and create a Social Media Post.
- Attached, Logo, sample flu social media image.
- TORVALE - must be included - in the colors provided (see attachment)
- Protect your community. Protect Your Elders. Stay Vaccinated. - must be include
-COVID-19 & flu - should be included
- image of child and women - should be included
-might include border
- inspiration https://brimtelo.org/, and https://www.facebook.com/Brimtelo

```html
<!DOCTYPE html>
<html lang="en">
<head>
<meta charset="utf-8">
<title>TORVALE – Flu &amp; COVID-19 Vaccination Campaign</title>
<link rel="stylesheet" href="https://fonts.googleapis.com/css2?family=Barlow:wght@600;800&family=Barlow+Semi+Condensed:wght@500;600&display=swap">
<style>
  :root {
    --teal: #4aa6b0;
    --teal-deep: #2f7f8c;
    --brick: #b4443a;
    --white: #ffffff;
    --sky: #3f8f9a;
    --crowd: #3c7f7a;
    --field: #2f8a4a;
    --field-deep: #24703b;
    --border-base: #c9d8d8;
    --border-accent: #8a6b70;
  }
  html, body {
    margin: 0;
    padding: 0;
    width: 1200px;
    height: 1200px;
    overflow: hidden;
    background: var(--white);
  }
  .post {
    position: relative;
    width: 1200px;
    height: 1200px;
    overflow: hidden;
    font-family: "Barlow", sans-serif;
  }
  .pattern-border {
    position: absolute;
    inset: 0;
    background: linear-gradient(135deg, var(--border-base), #e6eeee 50%, var(--border-base));
    box-shadow: inset 0 0 0 6px var(--border-accent);
  }
  .event-photo {
    position: absolute;
    left: 37px;
    top: 37px;
    width: 1126px;
    height: 1126px;
    background:
      radial-gradient(ellipse 30% 45% at 76% 50%, rgba(40, 70, 180, 0.55), transparent 70%),
      radial-gradient(ellipse 14% 35% at 18% 70%, rgba(90, 130, 190, 0.45), transparent 70%),
      linear-gradient(180deg, var(--sky) 0%, var(--crowd) 33%, var(--field) 55%, var(--field-deep) 100%);
  }
  .campaign-title {
    position: absolute;
    left: 79px;
    top: 78px;
    width: 746px;
    height: 205px;
    box-sizing: border-box;
    border: 6px solid var(--white);
  }
  .campaign-name {
    position: absolute;
    left: 44px;
    top: 2px;
    margin: 0;
    font-family: "Barlow", sans-serif;
    font-weight: 600;
    font-size: 168px;
    line-height: 1;
    letter-spacing: 2px;
    color: var(--teal);
    opacity: 0.92;
  }
  .campaign-subtitle {
    position: absolute;
    left: 125px;
    top: 254px;
    width: 648px;
    height: 50px;
    background: var(--white);
    display: flex;
    align-items: center;
    justify-content: center;
    margin: 0;
    font-family: "Barlow Semi Condensed", sans-serif;
    font-weight: 600;
    font-size: 32px;
    letter-spacing: 1.5px;
    color: var(--brick);
  }
  .org-mark {
    position: absolute;
    left: 861px;
    top: 77px;
    width: 254px;
    height: 206px;
    background: var(--white);
    display: flex;
    flex-direction: column;
    align-items: center;
    justify-content: center;
    gap: 14px;
  }
  .org-mark-square {
    width: 46px;
    height: 46px;
    background: var(--teal);
  }
  .org-mark-name {
    margin: 0;
    font-family: "Barlow", sans-serif;
    font-weight: 600;
    font-size: 30px;
    letter-spacing: 1px;
    color: var(--brick);
    text-align: center;
    line-height: 1.05;
  }
  .call-to-action {
    position: absolute;
    left: 102px;
    top: 578px;
    margin: 0;
    font-family: "Barlow", sans-serif;
    font-weight: 800;
    font-size: 88px;
    line-height: 158px;
    color: var(--white);
    letter-spacing: -0.5px;
  }
  .call-to-action span { display: block; }
</style>
</head>
<body>
  <main class="post">
    <div class="pattern-border" role="img" aria-label="Woven zigzag pattern border in grey, teal and muted red"></div>
    <div class="event-photo" role="img" aria-label="Photo seen from behind of a young girl and a woman in colourful regalia with a fringed blue shawl walking across a grass field at a powwow, tinted teal"></div>

    <div class="campaign-title">
      <h1 class="campaign-name">TORVALE</h1>
    </div>
    <p class="campaign-subtitle">FLU &amp; COVID -19 VACCINATION CAMPAIGN</p>

    <div class="org-mark">
      <div class="org-mark-square"></div>
      <p class="org-mark-name">BRIMTELO<br>ELDERS ALLIANCE</p>
    </div>

    <h2 class="call-to-action">
      <span>Protect Your Community.</span>
      <span>Protect Your Elders.</span>
      <span>Stay Vaccinated.</span>
    </h2>
  </main>
</body>
</html>
```